existing Business Card Re design

We are wanting to re design our cards to reflect our new logo , i have attache the current business cards and new logo
i will need a business card that reflects the following information on each card.

card 1:
Gordon Thibeaux, President
555-182-4407
info@qlmcoatingpro.example

card 2:
Lionel Ostrander, Outside Sales
Office: 555-182-4407
Cell: 555-631-2958
Sales@qlmcoatingpro.example

Card 3
Tomas Varley, Branch Manager
Office: 555-182-4407
Cell: 555-274-8163
Tomas@qlmcoatingpro.example

Card 4
I will need a Generic card with no name on it just business
555-182-4407
info@qlmcoatingpro.example

Target Market(s)

Homeowners and Contractors

Contact Information for Business Card

We are wanting to re design our cards to reflect our new logo , i have attache the current business cards and new logo. same info on current card

card 1:
Gordon Thibeaux, President
555-182-4407
info@qlmcoatingpro.example

card 2:
Office: 555-182-4407
Cell: 555-631-2958
Sales@qlmcoatingpro.example

Card 3
Office: 555-182-4407
Cell: 555-274-8163
Tomas@qlmcoatingpro.example

Card 4
555-182-4407
info@qlmcoatingpro.example

Requirements
Must have
• same info as current cards with a added business
"sanitizing"

```html
<!DOCTYPE html>
<html lang="en">
<head>
<meta charset="utf-8">
<title>Quillmark Coating Pro – Business Card</title>
<link rel="stylesheet" href="https://fonts.googleapis.com/css2?family=Montserrat:wght@400;500;700&display=swap">
<style>
  :root {
    --backdrop: #ececec;
    --card-white: #ffffff;
    --card-black: #262424;
    --brand-blue: #1f73c4;
    --ink: #1c1c1c;
    --ink-soft: #3a3a3a;
    --on-dark: #ffffff;
  }
  * { margin: 0; padding: 0; box-sizing: border-box; }
  html, body {
    width: 1200px;
    height: 800px;
    overflow: hidden;
    background: var(--backdrop);
    font-family: "Montserrat", sans-serif;
  }
  .sheet {
    width: 1200px;
    height: 800px;
    display: flex;
    align-items: center;
    justify-content: center;
    gap: 60px;
  }
  .card {
    position: relative;
    width: 525px;
    height: 300px;
    box-shadow: 0 2px 10px rgba(0, 0, 0, 0.12);
  }
  .card--front { background: var(--card-white); }
  .card--back {
    background: var(--card-black);
    display: flex;
    align-items: center;
    justify-content: center;
  }

  .brand {
    display: flex;
    align-items: center;
    gap: 10px;
    font-weight: 700;
    letter-spacing: 0.01em;
  }
  .brand__mark {
    width: 22px;
    height: 22px;
    background: var(--brand-blue);
    flex: none;
  }
  .brand__name { font-size: 22px; line-height: 1; }
  .card--front .brand {
    position: absolute;
    top: 40px;
    left: 38px;
    color: var(--ink);
  }
  .card--back .brand { color: var(--on-dark); }
  .card--back .brand__mark { width: 28px; height: 28px; }
  .card--back .brand__name { font-size: 28px; }

  .contact {
    position: absolute;
    left: 232px;
    top: 150px;
    color: var(--ink-soft);
  }
  .contact__name {
    font-size: 19px;
    font-weight: 500;
    color: var(--brand-blue);
    text-transform: uppercase;
    letter-spacing: 0.02em;
    line-height: 1.1;
  }
  .contact__role {
    font-size: 13px;
    margin-bottom: 12px;
    line-height: 1.3;
  }
  .contact__list { list-style: none; }
  .contact__item {
    display: flex;
    align-items: center;
    gap: 7px;
    font-size: 12.5px;
    line-height: 1.55;
  }
  .contact__icon {
    width: 10px;
    height: 10px;
    flex: none;
    fill: none;
    stroke: var(--brand-blue);
    stroke-width: 1.6;
    stroke-linecap: round;
    stroke-linejoin: round;
  }
</style>
</head>
<body>
<main class="sheet">
  <section class="card card--front" aria-label="Business card front">
    <div class="brand">
      <span class="brand__mark"></span>
      <span class="brand__name">Quillmark Coating Pro</span>
    </div>
    <div class="contact">
      <p class="contact__name">Lionel Ostrander</p>
      <p class="contact__role">Outside Sales</p>
      <ul class="contact__list">
        <li class="contact__item">
          <svg class="contact__icon" viewBox="0 0 10 10" aria-hidden="true"><path d="M2 1 L3.6 1 L4.2 3 L3.2 3.8 Q4.2 5.8 6.2 6.8 L7 5.8 L9 6.4 L9 8 Q5 9 2.5 6.5 Q0.5 4 2 1 Z"/></svg>
          <span>555-182-4407</span>
        </li>
        <li class="contact__item">
          <svg class="contact__icon" viewBox="0 0 10 10" aria-hidden="true"><rect x="2.5" y="0.8" width="5" height="8.4" rx="0.8"/><path d="M4.4 7.6 H5.6"/></svg>
          <span>555-631-2958</span>
        </li>
        <li class="contact__item">
          <svg class="contact__icon" viewBox="0 0 10 10" aria-hidden="true"><rect x="0.8" y="2" width="8.4" height="6" rx="0.6"/><path d="M1 2.4 L5 5.4 L9 2.4"/></svg>
          <span>Sales@qlmcoatingpro.example</span>
        </li>
      </ul>
    </div>
  </section>

  <section class="card card--back" aria-label="Business card back">
    <div class="brand">
      <span class="brand__mark"></span>
      <span class="brand__name">Quillmark Coating Pro</span>
    </div>
  </section>
</main>
</body>
</html>
```